Bimvoro Power Point Presentation

We need our presentation designed. Our current presentation is inconsistent, too text heavy, and complicated. We want this to be clean, sleek, and impressive as our references attached are.

Our colors are blue, black, and white.
Our font is roboto.

```html
<!DOCTYPE html>
<html lang="en">
<head>
<meta charset="utf-8">
<title>Bimvoro Media Kit 2021</title>
<link href="https://fonts.googleapis.com/css2?family=Roboto:wght@300;400;500;700&display=swap" rel="stylesheet">
<style>
:root{
  --blue:#1591f5;
  --blue-deep:#0b6fd0;
  --blue-light:#7cc0fa;
  --blue-pale:#e6f2fe;
  --ink:#1b2431;
  --ink-soft:#2c3645;
  --black:#000;
  --white:#fff;
  --grey:#eef0f3;
  --text:#333a44;
}
*{box-sizing:border-box;margin:0;padding:0}
html,body{width:1200px;height:2453px;overflow:hidden;background:var(--black)}
body{position:relative;font-family:'Roboto',sans-serif;color:var(--white)}

.brand{position:absolute;display:flex;align-items:center;gap:5px;font-family:'Roboto',sans-serif;font-weight:500;color:var(--white);white-space:nowrap}
.brand-mark{display:block;background:currentColor;border-radius:3px}
.brand--page{left:30px;top:34px;font-size:19px}
.brand--page .brand-mark{width:20px;height:20px}

.slide{position:absolute;width:540px;height:304px;overflow:hidden;background:var(--blue)}
.slide--hero{left:225px;top:118px;transform:scale(1.3889);transform-origin:0 0}

.footer-band{position:absolute;left:0;bottom:0;width:100%;height:18px;background:var(--ink);font-size:5.5px;font-weight:500;display:flex;align-items:center;justify-content:center}
.footer-band span{color:var(--blue)}

.title-block .brand{left:42px;top:44px;font-size:20px}
.title-block .brand-mark{width:24px;height:24px}
.deck-title{position:absolute;left:40px;top:114px;font-size:22px;font-weight:700;line-height:1.12}
.deck-date{position:absolute;left:40px;top:173px;font-size:6px}
.buy-button{position:absolute;left:42px;top:228px;width:98px;height:15px;border-radius:3px;background:#5fb3f8;box-shadow:0 2px 0 rgba(255,255,255,.7);font-size:5.5px;font-weight:700;display:flex;align-items:center;justify-content:center;letter-spacing:.2px}

.photo{position:absolute}
.photo--portal{left:259px;top:33px;width:247px;height:210px;border-radius:60px 20px 60px 20px;background:linear-gradient(120deg,#e9eef2 0%,#c9d3dc 45%,#3a3f47 75%,#1c76d6 100%)}
.photo--wash{inset:0;background:linear-gradient(90deg,var(--blue) 0%,rgba(21,145,245,.9) 45%,#3f7fbf 75%,#5c86ad 100%)}
.photo-grid{position:absolute;left:290px;top:0;width:250px;height:286px;background:var(--white)}
.photo-grid .tile{position:absolute}

.page-footer .brand{left:16px;bottom:11px;font-size:13px;color:var(--blue)}
.page-footer .brand-mark{width:14px;height:14px}
.progress{position:absolute;left:98px;right:12px;bottom:14px;height:8px;background:var(--grey)}
.page-no{position:absolute;right:14px;bottom:13px;width:12px;height:10px;background:var(--blue);color:var(--white);font-size:5.5px;font-weight:700;display:flex;align-items:center;justify-content:center;border-radius:1px}

.slide--white{background:var(--white);color:var(--ink)}
.head-mark{position:absolute;width:22px;height:22px;background:var(--blue);border-radius:3px}
.slide-heading{position:absolute;left:60px;top:26px;font-size:20px;font-weight:700;color:var(--ink)}
.slide-sub{position:absolute;left:60px;top:52px;font-size:12.5px;font-weight:300;color:var(--blue)}

.why-intro{position:absolute;left:0;top:0;width:269px;height:304px;text-align:center}
.why-intro .head-mark{left:124px;top:80px}
.why-intro h2{position:absolute;left:0;width:269px;top:110px;font-size:20px;font-weight:700}
.why-intro p{position:absolute;left:38px;width:193px;top:148px;font-size:10px;line-height:1.2;color:var(--blue);font-weight:300}
.why-col{position:absolute;top:0;width:135px;height:304px;text-align:center;color:var(--white)}
.why-col--special{left:269px;background:var(--blue)}
.why-col--powerful{left:404px;background:linear-gradient(180deg,#2d3748 0%,#1e2735 60%,#151c27 100%)}
.why-col h3{position:absolute;left:0;width:100%;top:20px;font-size:10.5px;font-weight:700}
.point{position:absolute;left:0;width:100%;display:flex;flex-direction:column;align-items:center;gap:5px;font-size:5.8px;line-height:1.2}
.point .icon{width:26px;height:26px;border-radius:50%;display:flex;align-items:center;justify-content:center}
.why-col--special .icon{background:var(--ink)}
.why-col--powerful .icon{background:var(--blue)}
.works{position:absolute;left:0;width:100%;top:180px;font-size:10.5px;font-weight:700}

.statement .brand{left:213px;top:84px;font-size:20px}
.statement .brand-mark{width:24px;height:24px}
.statement p{position:absolute;left:60px;width:420px;top:120px;text-align:center;font-size:16.5px;font-weight:300;line-height:1.18}

.advertiser-band{position:absolute;left:0;top:111px;width:540px;height:193px;background:linear-gradient(90deg,var(--blue) 0%,#2a8fe6 50%,var(--blue) 100%)}
.logo-wall{position:absolute;left:27px;top:22px;display:grid;grid-template-columns:repeat(8,50px);grid-auto-rows:46px;column-gap:12.6px;row-gap:17px}
.logo-tile{background:var(--white);border-radius:8px;display:flex;align-items:center;justify-content:center;font-size:7.5px;font-weight:500;color:var(--ink)}
.advertiser-band .brand{left:16px;bottom:11px;font-size:13px}
.advertiser-band .brand-mark{width:14px;height:14px}
.advertiser-band .progress{background:rgba(255,255,255,.9)}
.advertiser-band .page-no{background:var(--blue);}

.takeaway-lead{position:absolute;left:38px;top:98px;font-size:12.5px;color:var(--blue);font-weight:400}
.takeaway-list{position:absolute;left:38px;top:126px;width:232px;list-style:none;font-size:7.6px;line-height:1.15;color:var(--text)}
.takeaway-list li{position:relative;padding-left:20px;margin-bottom:7px}
.takeaway-list li::before{content:"✓";position:absolute;left:0;top:-1px;color:var(--blue);font-size:7px}
.promise-card{position:absolute;left:293px;top:40px;width:221px;height:193px;background:var(--blue);border-radius:34px 24px 34px 24px;display:flex;align-items:center;justify-content:center;text-align:center;color:var(--white);font-size:14px;font-weight:700;line-height:1.6}

.spec-table{position:absolute;left:25px;top:93px;width:489px;border-collapse:collapse;font-size:5.8px;color:var(--text)}
.spec-table th{height:23px;text-align:left;padding-left:4px;font-size:8px;font-weight:700;color:var(--white)}
.spec-table th.col-network{background:var(--blue)}
.spec-table th.col-content{background:var(--ink)}
.spec-table th.col-play{background:var(--blue-light)}
.spec-table td{height:25px;padding:0 5px;border:1px solid #dde3ea;vertical-align:middle;width:33.3%}
.spec-table td.tick::before{content:"✓ ";color:var(--blue)}

.thanks .photo--wash{background:linear-gradient(120deg,#1a86e8 0%,#2f7ccf 45%,#24558f 80%,#173c6a 100%)}
.thanks .brand{left:58px;top:128px;font-size:20px}
.thanks .brand-mark{width:24px;height:24px}
.thanks h2{position:absolute;left:57px;top:180px;font-size:25px;font-weight:700}
.thanks p{position:absolute;left:58px;top:216px;font-size:10px}
</style>
</head>
<body>

<div class="brand brand--page"><i class="brand-mark"></i>Bimvoro</div>

<!-- Hero cover -->
<section class="slide slide--hero title-block">
  <div class="photo photo--portal" role="img" aria-label="Traveller looking at an indoor digital screen in a bright terminal"></div>
  <div class="brand"><i class="brand-mark"></i>Bimvoro</div>
  <h1 class="deck-title">Indoor DOOH<br>Audiences at Scale</h1>
  <div class="deck-date">Monday, November 29, 2021</div>
  <div class="buy-button">BUY ON BIMVORO</div>
  <div class="footer-band">Info@<span>Bimvoro</span>.com&nbsp;|&nbsp;<span>MEDIA KIT</span>&nbsp;2021</div>
</section>

<!-- Cover A -->
<section class="slide title-block" style="left:51px;top:810px">
  <div class="photo photo--portal" role="img" aria-label="Traveller looking at an indoor digital screen in a bright terminal"></div>
  <div class="brand"><i class="brand-mark"></i>Bimvoro</div>
  <h1 class="deck-title">Indoor DOOH<br>Audiences at Scale</h1>
  <div class="deck-date">Monday, November 29, 2021</div>
  <div class="buy-button">BUY ON BIMVORO</div>
  <div class="footer-band">Info@<span>Bimvoro</span>.com&nbsp;|&nbsp;<span>MEDIA KIT</span>&nbsp;2021</div>
</section>

<!-- Cover B -->
<section class="slide title-block" style="left:609px;top:810px">
  <div class="photo-grid">
    <div class="tile" role="img" aria-label="Staff preparing food at a counter" style="left:4px;top:10px;width:82px;height:82px;background:linear-gradient(135deg,#d9d4cc,#8a7a6a)"></div>
    <div class="tile" role="img" aria-label="Person using a tablet with charts" style="left:91px;top:10px;width:159px;height:82px;background:linear-gradient(135deg,#5a4035,#c9b9ae)"></div>
    <div class="tile" role="img" aria-label="Traveller at an indoor digital screen" style="left:4px;top:102px;width:159px;height:82px;background:linear-gradient(135deg,#e3e6ea,#8f96a0)"></div>
    <div class="tile" role="img" aria-label="Guests dining in a warm restaurant" style="left:168px;top:102px;width:82px;height:82px;background:linear-gradient(135deg,#4b2b1f,#a86a3f)"></div>
    <div class="tile" role="img" aria-label="Screen mounted in a fast food venue" style="left:4px;top:194px;width:82px;height:82px;background:linear-gradient(135deg,#b6352d,#e6e2dc)"></div>
    <div class="tile" role="img" aria-label="Reception desk in a clinic" style="left:91px;top:194px;width:159px;height:82px;background:linear-gradient(135deg,#ece6df,#7e6f62)"></div>
  </div>
  <div class="brand"><i class="brand-mark"></i>Bimvoro</div>
  <h1 class="deck-title">Indoor DOOH<br>Audiences at Scale</h1>
  <div class="deck-date">Monday, November 29, 2021</div>
  <div class="buy-button">BUY ON BIMVORO</div>
  <div class="footer-band">Info@<span>Bimvoro</span>.com&nbsp;|&nbsp;<span>MEDIA KIT</span>&nbsp;2021</div>
</section>

<!-- Cover C -->
<section class="slide title-block" style="left:51px;top:1132px">
  <div class="photo photo--wash" role="img" aria-label="Blue-tinted terminal with a wall-mounted digital screen"></div>
  <div class="brand"><i class="brand-mark"></i>Bimvoro</div>
  <h1 class="deck-title" style="top:120px">Indoor DOOH<br>Audiences at Scale</h1>
  <div class="deck-date" style="top:180px">Monday, November 29, 2021</div>
  <div class="buy-button">BUY ON BIMVORO</div>
  <div class="footer-band">Info@<span>Bimvoro</span>.com&nbsp;|&nbsp;<span>MEDIA KIT</span>&nbsp;2021</div>
</section>

<!-- Why go indoor -->
<section class="slide slide--white" style="left:609px;top:1132px">
  <div class="why-intro">
    <i class="head-mark"></i>
    <h2>Why Go Indoor</h2>
    <p>it’s not just lockdowns ending - recent uptick has been driven by the unique effectiveness of indoor DOOH ad exposure.</p>
  </div>
  <div class="why-col why-col--special">
    <h3>It’s special...</h3>
    <div class="point" style="top:40px"><span class="icon"><svg width="14" height="10" viewBox="0 0 14 10"><path d="M1 5C3 1.5 11 1.5 13 5 11 8.5 3 8.5 1 5Z" fill="#fff"/><circle cx="7" cy="5" r="2" fill="#1b2431"/></svg></span>Dwell time measured in<br>minutes, not seconds</div>
    <div class="point" style="top:95px"><span class="icon" style="font-size:13px;font-weight:700">$</span>Brand-safe</div>
    <div class="point" style="top:150px"><span class="icon"><svg width="12" height="13" viewBox="0 0 12 13"><circle cx="6" cy="4" r="3" fill="#fff"/><path d="M0 13C0 8 12 8 12 13Z" fill="#fff"/></svg></span>100% viewability by<br>humans, not bots</div>
    <div class="point" style="top:205px"><span class="icon"><svg width="12" height="12" viewBox="0 0 12 12"><rect x="1" y="1" width="10" height="10" rx="2" fill="none" stroke="#fff" stroke-width="1.6"/><circle cx="6" cy="6" r="2" fill="#fff"/></svg></span>Not<br>Skippable</div>
  </div>
  <div class="why-col why-col--powerful" role="img" aria-label="Dim photo of people in an indoor venue">
    <h3>It’s powerful...</h3>
    <div class="point" style="top:40px"><span class="icon"><svg width="13" height="12" viewBox="0 0 13 12"><path d="M1 4H4L9 1V11L4 8H1Z" fill="#fff"/></svg></span>Engaged impressions, consumer<br>attention, means...</div>
    <div class="point" style="top:97px"><span class="icon"><svg width="14" height="14" viewBox="0 0 14 14"><circle cx="7" cy="7" r="5.5" fill="none" stroke="#fff" stroke-width="1.3"/><circle cx="7" cy="7" r="2" fill="#fff"/></svg></span>...Indoor DOOH 2x more likely to be<br>seen, recalled, than traditional OOH1</div>
    <div class="works">And it works.</div>
    <div class="point" style="top:210px"><span class="icon"><svg width="13" height="13" viewBox="0 0 13 13"><path d="M2.5 6.5A4 4 0 0 1 10 4.5M10.5 6.5A4 4 0 0 1 3 8.5" fill="none" stroke="#fff" stroke-width="1.5"/><path d="M10.5 1.5V5H7Z M2.5 11.5V8H6Z" fill="#fff"/></svg></span>2x increase in reach if added to<br>Omni-Channel campaigns2</div>
  </div>
  <div class="page-footer">
    <div class="brand"><i class="brand-mark"></i>Bimvoro</div>
    <div class="progress" style="background:rgba(238,240,243,.85)"></div>
    <div class="page-no">4</div>
  </div>
</section>

<!-- Statement -->
<section class="slide statement" style="left:51px;top:1454px">
  <div class="photo photo--wash" role="img" aria-label="Blue-tinted terminal with a wall-mounted digital screen" style="background:linear-gradient(90deg,#1a8cf0 0%,#3a86d4 55%,#2f78c4 100%)"></div>
  <div class="brand"><i class="brand-mark"></i>Bimvoro</div>
  <p>Bimvoro offers advertisers easy, affordable access to North America’s largest indoor DOOH network, containing diverse audience segments while captivated in indoor environments</p>
</section>

<!-- Advertisers -->
<section class="slide slide--white" style="left:609px;top:1454px">
  <i class="head-mark" style="left:25px;top:25px"></i>
  <h2 class="slide-heading">Advertisers</h2>
  <div class="slide-sub">Brands that buy on our network.</div>
  <div class="advertiser-band">
    <div class="logo-wall">
      <div class="logo-tile">Norvik</div><div class="logo-tile">Pellaro</div><div class="logo-tile">Tandrel</div><div class="logo-tile">Quillow</div>
      <div class="logo-tile">Brevan</div><div class="logo-tile">Ostrin</div><div class="logo-tile">Calvesse</div><div class="logo-tile">Medrano</div>
      <div class="logo-tile">Fjolvik</div><div class="logo-tile">Crunzo</div><div class="logo-tile">Vellano</div><div class="logo-tile">Kitori</div>
      <div class="logo-tile">Aldmere</div><div class="logo-tile">Sonaro</div><div class="logo-tile">Rivbank</div><div class="logo-tile">Runvale</div>
    </div>
    <div class="brand"><i class="brand-mark"></i>Bimvoro</div>
    <div class="progress"></div>
    <div class="page-no">6</div>
  </div>
</section>

<!-- Key takeaways -->
<section class="slide slide--white" style="left:51px;top:1775px">
  <i class="head-mark" style="left:25px;top:25px"></i>
  <h2 class="slide-heading">Key Takeaways</h2>
  <div class="takeaway-lead">Bimvoro is:</div>
  <ul class="takeaway-list">
    <li>North America’s largest and fastest-growing indoor DOOH screen network</li>
    <li>Powerful enough to capture the attention of nationwide audiences at scale, specific enough to provide access to diverse audience segments</li>
    <li>Programmatically-accessible, ensuring cost-efficiency, transparency and real-time optimizations</li>
    <li>Flexible enough to get any DOOH campaign or integration up and running quickly and without issue</li>
  </ul>
  <div class="promise-card">The Right Time.<br>The Right Message.<br>The Right Audience.</div>
  <div class="page-footer">
    <div class="brand"><i class="brand-mark"></i>Bimvoro</div>
    <div class="progress"></div>
    <div class="page-no">7</div>
  </div>
</section>

<!-- Digital media formats -->
<section class="slide slide--white" style="left:609px;top:1775px">
  <i class="head-mark" style="left:25px;top:25px"></i>
  <h2 class="slide-heading">Digital Media Formats</h2>
  <div class="slide-sub">Specifications</div>
  <table class="spec-table">
    <tr><th class="col-network">Network</th><th class="col-content">Content Specifications</th><th class="col-play">Ad Content Play Suggestions</th></tr>
    <tr><td class="tick">Indoor, 32 –73” Screens</td><td class="tick">1920 pixels (w) x 1080 pixels (h) 16:9</td><td class="tick">15 second</td></tr>
    <tr><td class="tick">Full Screen Take Over</td><td class="tick">1080 pixels (w) x 1920 pixels (h) 9:16</td><td class="tick">30 second</td></tr>
    <tr><td class="tick">Sold programmatically</td><td class="tick">Static: PNG, RGB, encoded. JPG or H.264</td><td class="tick">60 second</td></tr>
    <tr><td class="tick">No Blacklisted Advertisers</td><td class="tick">Video: .MP5 / encoded .MOV</td><td></td></tr>
    <tr><td class="tick">Approval Upon Venue Review</td><td class="tick">Will repurpose TV spots, banner ads; transcode ill-fitting static creatives</td><td></td></tr>
  </table>
  <div class="page-footer">
    <div class="brand"><i class="brand-mark"></i>Bimvoro</div>
    <div class="progress"></div>
    <div class="page-no">8</div>
  </div>
</section>

<!-- Thank you -->
<section class="slide thanks" style="left:330px;top:2097px">
  <div class="photo photo--wash" role="img" aria-label="Blue-tinted handshake between two business people"></div>
  <div class="brand"><i class="brand-mark"></i>Bimvoro</div>
  <h2>Thank You!</h2>
  <p>for your Time and Attention ...</p>
  <div class="footer-band">Info@<span>Bimvoro</span>.com&nbsp;|&nbsp;<span>MEDIA KIT</span>&nbsp;2021</div>
</section>

</body>
</html>
```